Lumora aesthetics offers a range of facial aesthetics treatments by a fully qualified dentist, to a high end crowd. Treatments include antiwrinkle treatment, the use of dermal fillers to provide facial volumisation and rejuvenation and also lip volumisation.
I want a luxurious and bold look. Black background with a bold striking gold logo in the centre possibly incorporating the outline of a face in a subtle yet effective way. I want it to include the work I offer so people will be aware of what they are looking into but not look like there's too much on the card, So it's a clean look.
At the bottom I would like it to say by Dr. Meera Sandhu. Alongside my email address and mobile number.

```html
<!DOCTYPE html>
<html lang="en">
<head>
<meta charset="utf-8">
<title>Lumora Aesthetics – Business Card</title>
<link rel="stylesheet" href="https://fonts.googleapis.com/css2?family=Montserrat:wght@600;700;800&family=Open+Sans:wght@400&display=swap">
<style>
  :root {
    --backdrop: #1b1b1c;
    --card: #1e1e1f;
    --gold: #e0c03a;
    --gold-soft: #f0d552;
    --text-light: #f2f2f2;
  }
  * { margin: 0; padding: 0; box-sizing: border-box; }
  html, body {
    width: 1200px;
    height: 1000px;
    overflow: hidden;
    background: var(--backdrop);
  }
  .canvas {
    position: relative;
    width: 1200px;
    height: 1000px;
    display: flex;
    align-items: center;
    justify-content: center;
  }
  .business-card {
    position: relative;
    width: 900px;
    height: 520px;
    background: var(--card);
    border-radius: 36px;
    box-shadow: 0 24px 60px rgba(0,0,0,0.55);
    overflow: hidden;
  }
  .brand {
    position: absolute;
    left: 250px;
    top: 110px;
    display: flex;
    align-items: flex-start;
    gap: 22px;
  }
  .brand-mark {
    width: 64px;
    height: 64px;
    border-radius: 50%;
    background: var(--gold);
    margin-top: 8px;
  }
  .brand-name {
    font-family: "Montserrat", sans-serif;
    font-weight: 800;
    color: var(--gold);
    line-height: 1.02;
    letter-spacing: 1px;
    text-transform: uppercase;
  }
  .brand-name .line-one { display: block; font-size: 64px; }
  .brand-name .line-two { display: block; font-size: 46px; margin-left: 40px; }

  .services {
    position: absolute;
    right: 60px;
    top: 200px;
    display: flex;
    align-items: stretch;
    gap: 18px;
  }
  .service-list {
    list-style: none;
    text-align: right;
    font-family: "Open Sans", sans-serif;
    font-size: 19px;
    color: var(--text-light);
    line-height: 1.9;
  }
  .service-bar {
    width: 5px;
    background: var(--gold);
  }

  .practitioner {
    position: absolute;
    left: 70px;
    top: 330px;
  }
  .practitioner-name {
    font-family: "Montserrat", sans-serif;
    font-weight: 600;
    font-size: 38px;
    color: var(--gold);
    margin-bottom: 14px;
  }
  .contact-list {
    list-style: none;
    font-family: "Open Sans", sans-serif;
    font-size: 19px;
    color: var(--text-light);
    line-height: 1.35;
  }
  .contact-item {
    display: flex;
    align-items: flex-start;
    gap: 14px;
    margin-bottom: 6px;
  }
  .contact-icon {
    width: 18px;
    height: 18px;
    flex: none;
    margin-top: 4px;
    fill: var(--gold);
  }
</style>
</head>
<body>
<main class="canvas">
  <section class="business-card" aria-label="Lumora Aesthetics business card">
    <div class="brand">
      <span class="brand-name">
        <span class="line-one">Lumora</span>
        <span class="line-two">Aesthetics</span>
      </span>
      <span class="brand-mark" aria-hidden="true"></span>
    </div>

    <div class="services">
      <ul class="service-list">
        <li>Facial Volumisation</li>
        <li>Rejuvenation</li>
        <li>Lip Volumisation</li>
      </ul>
      <span class="service-bar" aria-hidden="true"></span>
    </div>

    <div class="practitioner">
      <h1 class="practitioner-name">Dr. Meera Sandhu</h1>
      <ul class="contact-list">
        <li class="contact-item">
          <svg class="contact-icon" viewBox="0 0 24 24" aria-hidden="true"><path d="M6.6 10.8a15.1 15.1 0 0 0 6.6 6.6l2.2-2.2c.3-.3.7-.4 1-.2 1.1.4 2.3.6 3.6.6.6 0 1 .4 1 1V20c0 .6-.4 1-1 1A17 17 0 0 1 3 4c0-.6.4-1 1-1h3.5c.6 0 1 .4 1 1 0 1.2.2 2.4.6 3.6.1.3 0 .7-.2 1z"/></svg>
          <span>+000 123 456 789</span>
        </li>
        <li class="contact-item">
          <svg class="contact-icon" viewBox="0 0 24 24" aria-hidden="true"><path d="M2 5h20v14H2z M2 5l10 8 10-8" fill="none" stroke="#e0c03a" stroke-width="2.4"/></svg>
          <span>urname@email.com</span>
        </li>
        <li class="contact-item">
          <svg class="contact-icon" viewBox="0 0 24 24" aria-hidden="true"><path d="M12 2a7 7 0 0 0-7 7c0 5.2 7 13 7 13s7-7.8 7-13a7 7 0 0 0-7-7zm0 9.5A2.5 2.5 0 1 1 12 6.5a2.5 2.5 0 0 1 0 5z"/></svg>
          <span>Your Street Address Here,<br>Country Name, 123</span>
        </li>
      </ul>
    </div>
  </section>
</main>
</body>
</html>
```